Wireless retailer specializing in sale / purchase of used and refurbished devices. We are an authorized dealer for " vCarda Wireless". Logos for vCarda and our logo have been included.
Business card needs to feature both locations address. We will do a reprint once we have the phone number for the second location and remove the "coming soon" text.
Cards will also need to be personalized per employee. Will post that information as well.
Any suggestions are welcome
Industry/Entity Type
Business
Contact Information for Business Card
The Signal Hut
Brenmoor Field Plaza Shopping Center
4871 Quarrel Lane
Virginia Beach, VA 23464
757.318.9264
Coming in 2014
The Signal Hut 2
Marlow Bexby Shopping Center
2619 Tessing Rd Suite #847
Virginia Beach, VA 23452
Look and feel
Each slider illustrates characteristics of the customer's brand and the style your logo design should communicate.

```html
<!DOCTYPE html>
<html lang="en">
<head>
<meta charset="utf-8">
<title>The Signal Hut — Business Card</title>
<link href="https://fonts.googleapis.com/css2?family=Exo+2:wght@300;400;700&display=swap" rel="stylesheet">
<style>
  :root {
    --stage: #161718;
    --card-front-top: #2e2f31;
    --card-front-bottom: #121314;
    --card-back: #2a2c2e;
    --teal: #1f8fa0;
    --white: #f2f4f5;
    --soft-white: #d9dcde;
    --divider: #4a4d50;
    --badge: #eceeef;
  }
  * { box-sizing: border-box; margin: 0; padding: 0; }
  html, body {
    width: 1200px;
    height: 3000px;
    overflow: hidden;
    background: var(--stage);
    font-family: "Exo 2", "Arial", sans-serif;
  }
  .canvas {
    position: relative;
    width: 1200px;
    height: 3000px;
  }

  /* Front of card */
  .card-front {
    position: absolute;
    left: 150px;
    top: 140px;
    width: 900px;
    height: 1575px;
    border-radius: 6px;
    overflow: hidden;
    background: linear-gradient(160deg, var(--card-front-top) 0%, var(--card-front-bottom) 100%);
  }
  .card-front .wordmark-pattern {
    position: absolute;
    inset: 0;
    background: linear-gradient(150deg, rgba(70,72,75,0.35) 0%, rgba(30,31,33,0.2) 55%, rgba(10,10,11,0.4) 100%);
  }
  .card-front .brand-name {
    position: absolute;
    left: 640px;
    top: 560px;
    transform-origin: 0 0;
    transform: rotate(90deg);
    color: var(--white);
    font-weight: 700;
    font-size: 120px;
    line-height: 1;
    letter-spacing: 4px;
    text-transform: uppercase;
    white-space: nowrap;
  }
  .card-front .brand-name span { display: block; }

  /* Back of card */
  .card-back {
    position: absolute;
    left: 75px;
    top: 1860px;
    width: 1050px;
    height: 600px;
    border-radius: 6px;
    background: var(--card-back);
    color: var(--soft-white);
  }
  .card-back .brand-name {
    position: absolute;
    left: 70px;
    top: 120px;
    color: var(--teal);
    font-weight: 700;
    font-size: 58px;
    letter-spacing: 3px;
    text-transform: uppercase;
    white-space: nowrap;
  }
  .card-back .partner-badge {
    position: absolute;
    right: 60px;
    top: 50px;
    width: 180px;
    height: 62px;
    border-radius: 6px;
    background: var(--badge);
  }
  .location {
    position: absolute;
    top: 330px;
    font-weight: 300;
    font-size: 25px;
    line-height: 1.42;
  }
  .location.primary { left: 70px; }
  .location.upcoming { left: 595px; top: 310px; }
  .location-label {
    color: var(--teal);
    font-weight: 400;
    text-transform: uppercase;
    letter-spacing: 1px;
  }
  .location-phone {
    margin-top: 14px;
    color: var(--teal);
    font-size: 36px;
    font-weight: 400;
    letter-spacing: 2px;
  }
  .card-back .column-divider {
    position: absolute;
    left: 555px;
    top: 315px;
    width: 1px;
    height: 215px;
    background: var(--divider);
  }
</style>
</head>
<body>
<main class="canvas">

  <section class="card-front">
    <div class="wordmark-pattern" role="img" aria-label="Faint repeated brand wordmark pattern across the card"></div>
    <h1 class="brand-name"><span>The Signal</span><span>Hut</span></h1>
  </section>

  <section class="card-back">
    <h2 class="brand-name">The Signal Hut</h2>
    <div class="partner-badge" role="img" aria-label="vCarda Wireless authorized retailer badge"></div>

    <address class="location primary">
      <div class="location-label">The Signal Hut</div>
      <div>Brenmoor Field Plaza Shopping Center</div>
      <div>4871 Quarrel Lane</div>
      <div>Virginia Beach, VA 23464</div>
      <div class="location-phone">757.318.9264</div>
    </address>

    <div class="column-divider"></div>

    <address class="location upcoming">
      <div class="location-label">Coming in 2014</div>
      <div>Marlow Bexby Shopping Center</div>
      <div>2619 Tessing Rd Suite #847</div>
      <div>Virginia Beach, VA 23452</div>
    </address>
  </section>

</main>
</body>
</html>
```